Template design for an Online "Membership Subscription" System

I need a template for a service that will allow website owners to create their own online subscription services and member portals.
With just a snippet of code they can password protect certain parts of their website.
Tagline:
"Monetize your website with TallowGateHubs"
"The Easiest Way To Turn Your Website Into 'Members Only'"
Call to action "Try For Free" and "Watch a demo"
Features:
1. Quick & easy to set up
2. Works with any website
3. Charge one-time or subscription fees
4. Automated billing, sign up and more
5. Customize to match your website
6. Unlimited members
Similar websites/services;
https://quillhavenvault.example
https://joinbrook.example
https://www.clubnestly.example
I'd like a clean looking, uncluttered design targeted towards "non-techie" people. Easy to read without a lot going on. Emphasizing ease of use and pushing towards a "Try for free" option.
Separate into sections with the top section having the tagline. Followed by feature overview, testimonials, sample use cases.
A footer with multiple links by industry that can provide a case study for various use cases;
Ex;
Clubs
Religious Organizations
Online Stores
Digital Products
Education
Coaching
Fitness
Target Market(s)
Non technical small business owners
Number of Pages Required
2 page
Look and feel

```html
<!DOCTYPE html>
<html lang="en">
<head>
<meta charset="utf-8">
<title>TallowGateHubs – Membership Subscriptions</title>
<link href="https://fonts.googleapis.com/css2?family=Poppins:wght@600;700&family=Roboto:wght@400;500;700&display=swap" rel="stylesheet">
<style>
:root{
  --primary:#0aa3dd;
  --deep:#0b4ea6;
  --ink:#1f2226;
  --muted:#666b72;
  --band:#f5f7fa;
  --footer:#03122c;
  --bar:#0a4fa5;
  --white:#ffffff;
  --star:#f6b500;
}
*{box-sizing:border-box;margin:0;padding:0}
html,body{width:685px;height:1200px;overflow:hidden}
body{position:relative;background:var(--white);font-family:"Roboto",sans-serif;color:var(--ink)}
.abs{position:absolute}
.top-rule{left:0;top:0;width:685px;height:3px;background:var(--primary)}
.brand{left:63px;top:17px;font-family:"Poppins",sans-serif;font-weight:700;font-size:15px;color:var(--ink)}
.nav a{position:absolute;top:22px;font-size:8.6px;color:var(--ink);text-decoration:none;letter-spacing:.1px}
.nav a.active{color:var(--primary)}
.nav a.active::after{content:"";position:absolute;left:0;right:0;bottom:-3px;height:1.5px;background:var(--primary)}
.btn{display:flex;align-items:center;justify-content:center;gap:5px;color:var(--white);font-weight:700;font-size:8.6px;border-radius:2px;text-transform:uppercase}
.btn svg{width:8px;height:8px}
.btn-primary{background:var(--primary)}
.btn-deep{background:var(--deep)}
.hero-title{left:62px;top:118px;font-family:"Poppins",sans-serif;font-weight:700;font-size:23.5px;line-height:31px;color:var(--ink)}
.slide-arrow{width:25px;height:24px;display:flex;align-items:center;justify-content:center;border-radius:2px;background:var(--white)}
.slide-arrow.prev{border:1px solid var(--primary)}
.slide-arrow.next{box-shadow:0 2px 6px rgba(0,0,0,.12)}
.art{border-radius:50%}
.features-band{left:0;top:373px;width:685px;height:319px;background:var(--band)}
.section-title{font-family:"Poppins",sans-serif;font-weight:700;color:var(--ink)}
.rule{height:1.5px;width:29px;background:var(--deep)}
.feature-list{left:397px;top:466px;list-style:none}
.feature-list li{display:flex;align-items:center;gap:8px;height:16px;margin-bottom:16.2px;font-size:11px;color:var(--ink)}
.feature-list svg{width:16px;height:16px;flex:none}
.card{top:779px;width:177px;height:127px;background:var(--white);box-shadow:0 1px 8px rgba(0,0,0,.1);padding:13px 13px 0}
.card p{font-size:7.8px;line-height:14.2px;color:var(--muted)}
.reviewer{position:absolute;left:13px;top:82px;display:flex;align-items:center;gap:5px}
.avatar{width:29px;height:29px;border-radius:50%;background:linear-gradient(135deg,#c9ced6,#8d97a5)}
.reviewer strong{display:block;font-size:8.6px;font-weight:500;color:var(--ink)}
.stars{color:var(--star);font-size:7px;letter-spacing:1px}
.quote{position:absolute;left:139px;top:76px;font-family:"Poppins",sans-serif;font-weight:700;font-size:44px;line-height:1;color:var(--primary)}
.footer{left:0;top:960px;width:685px;height:212px;background:var(--footer);color:var(--white)}
.footer h4{position:absolute;top:47px;font-size:10.3px;font-weight:700}
.footer ul{position:absolute;top:73px;list-style:none}
.footer li{font-size:8.8px;height:18.6px}
.contact-row{position:absolute;left:308px;display:flex;align-items:flex-start;gap:6px;font-size:8.8px;line-height:12px}
.contact-row .dot{width:16px;height:16px;border-radius:50%;background:var(--white);display:flex;align-items:center;justify-content:center;flex:none}
.contact-row .dot svg{width:8px;height:8px}
.newsletter-copy{left:477px;top:1035px;font-size:8.8px;line-height:12px;color:var(--white);width:160px}
.subscribe{left:477px;top:1074px;width:144px;height:21px;background:var(--white);border-radius:11px;overflow:hidden;display:flex}
.subscribe span{flex:1;font-size:5.5px;color:#555;display:flex;align-items:center;padding-left:9px;gap:3px}
.subscribe b{width:27px;background:var(--primary);display:flex;align-items:center;justify-content:center}
.social{top:1107px;width:19px;height:19px;border-radius:50%;background:var(--white)}
.social::after{content:"";position:absolute;left:7px;top:7px;width:5px;height:5px;border-radius:50%;background:var(--primary)}
.copyright{left:0;top:1172px;width:685px;height:28px;background:var(--bar);color:var(--white);font-size:7.8px;display:flex;align-items:center;justify-content:center}
</style>
</head>
<body>
<div class="abs top-rule"></div>

<header>
  <div class="abs brand">TallowGateHubs</div>
  <nav class="nav">
    <a class="active" style="left:222px">HOME</a>
    <a style="left:259px">ABOUT US</a>
    <a style="left:316px">FEATURES</a>
    <a style="left:373px">TESTIMONIALS</a>
    <a style="left:449px">CONTACT US</a>
  </nav>
  <a class="abs btn btn-primary" style="left:534px;top:15px;width:87px;height:25px">Get Started
    <svg viewBox="0 0 10 10"><circle cx="5" cy="5" r="5" fill="#fff"/><path d="M3 5h4M5.3 3.2 7 5 5.3 6.8" stroke="#0aa3dd" stroke-width="1.3" fill="none"/></svg></a>
</header>

<section class="hero">
  <h1 class="abs hero-title">The Easiest Way To<br>Turn Your Website Into<br>Members Only</h1>
  <a class="abs btn btn-primary" style="left:62px;top:227px;width:92px;height:25px">Try For Free
    <svg viewBox="0 0 10 10"><circle cx="5" cy="5" r="5" fill="#fff"/><path d="M3 5h4M5.3 3.2 7 5 5.3 6.8" stroke="#0aa3dd" stroke-width="1.3" fill="none"/></svg></a>
  <a class="abs btn btn-deep" style="left:160px;top:227px;width:93px;height:25px">Watch A Demo
    <svg viewBox="0 0 10 10"><circle cx="5" cy="5" r="5" fill="#fff"/><path d="M3 5h4M5.3 3.2 7 5 5.3 6.8" stroke="#0b4ea6" stroke-width="1.3" fill="none"/></svg></a>
  <div class="abs slide-arrow prev" style="left:61px;top:280px"><svg width="12" height="8" viewBox="0 0 12 8"><path d="M11 4H1M4 1 1 4l3 3" stroke="#0b4ea6" stroke-width="1.4" fill="none"/></svg></div>
  <div class="abs slide-arrow next" style="left:91px;top:280px"><svg width="12" height="8" viewBox="0 0 12 8"><path d="M1 4h10M8 1l3 3-3 3" stroke="#0b4ea6" stroke-width="1.4" fill="none"/></svg></div>
  <div class="abs art" role="img" aria-label="Illustration of a laptop showing a web page with a man using a megaphone beside it" style="left:345px;top:80px;width:315px;height:252px;background:radial-gradient(circle at 45% 55%,#3f6fd1 0 22%,#bcd2f0 38%,#e9f1fb 62%,rgba(240,245,252,0) 72%)"></div>
</section>

<section>
  <div class="abs features-band"></div>
  <div class="abs art" role="img" aria-label="Illustration of people analysing charts on a large dashboard and a phone with social reactions" style="left:27px;top:418px;width:338px;height:228px;background:radial-gradient(ellipse at 50% 50%,#ffffff 0 26%,#4a6fc0 27% 30%,#d9e6f9 45%,rgba(245,247,250,0) 70%)"></div>
  <h2 class="abs section-title" style="left:397px;top:416px;font-size:17.6px">Features</h2>
  <div class="abs rule" style="left:397px;top:443px"></div>
  <ul class="abs feature-list">
    <li><svg viewBox="0 0 16 16" fill="none" stroke="#0aa3dd" stroke-width="1"><circle cx="9" cy="9" r="5.5"/><path d="M9 6v3l2 1M8 2.5h2M1 8h2M1 11h2"/></svg>Quick &amp; easy to set up</li>
    <li><svg viewBox="0 0 16 16" fill="none" stroke="#0aa3dd" stroke-width="1"><circle cx="8" cy="8" r="6.5"/><ellipse cx="8" cy="8" rx="3" ry="6.5"/><path d="M1.5 8h13M2.5 5h11M2.5 11h11"/></svg>Works with any website</li>
    <li><svg viewBox="0 0 16 16" fill="none" stroke="#0aa3dd" stroke-width="1"><rect x="1.5" y="2" width="10" height="8"/><rect x="5" y="7" width="9.5" height="7"/><path d="M7 10h5"/></svg>Charge one-time or subscription fees</li>
    <li><svg viewBox="0 0 16 16" fill="none" stroke="#0aa3dd" stroke-width="1"><rect x="1.5" y="2" width="13" height="4"/><rect x="3.5" y="6" width="9" height="8.5"/><circle cx="8" cy="10" r="2"/></svg>Automated billing, sign up and more</li>
    <li><svg viewBox="0 0 16 16" fill="none" stroke="#0aa3dd" stroke-width="1"><rect x="1.5" y="3" width="12" height="10"/><path d="M1.5 6h12M4 9h4M4 11h6"/><circle cx="13" cy="4" r="2.2"/></svg>Customize to match your website</li>
    <li><svg viewBox="0 0 16 16" fill="none" stroke="#0aa3dd" stroke-width="1"><circle cx="8" cy="3.5" r="1.6"/><circle cx="4" cy="8" r="1.6"/><circle cx="12" cy="8" r="1.6"/><path d="M1.5 14c0-2 1-3 2.5-3s2.5 1 2.5 3M9.5 14c0-2 1-3 2.5-3s2.5 1 2.5 3M5.5 9c0-2 1-3 2.5-3s2.5 1 2.5 3"/></svg>Unlimited members</li>
  </ul>
</section>

<section>
  <h2 class="abs section-title" style="left:0;width:685px;text-align:center;top:732px;font-size:18.6px">Our Testimonials</h2>
  <div class="abs rule" style="left:328px;top:759px"></div>

  <article class="abs card" style="left:63px">
    <p>Lorem ipsum dolor sit amet, consectetur adipiscing elitedsed do eiusmod tempor incididunt uted labore ete dolore magna minim veniamed, quised aliquad.</p>
    <div class="reviewer"><div class="avatar" role="img" aria-label="Reviewer portrait"></div><div><strong>Dana Holloway</strong><span class="stars">★★★★★</span></div></div>
    <span class="quote">“</span>
  </article>
  <article class="abs card" style="left:254px">
    <p>Lorem ipsum dolor sit amet, consectetur adipiscing elitedsed do eiusmod tempor incididunt uted labore ete dolore magna minim veniamed, quised aliquad.</p>
    <div class="reviewer"><div class="avatar" role="img" aria-label="Reviewer portrait"></div><div><strong>Dana Holloway</strong><span class="stars">★★★★★</span></div></div>
    <span class="quote">“</span>
  </article>
  <article class="abs card" style="left:445px">
    <p>Lorem ipsum dolor sit amet, consectetur adipiscing elitedsed do eiusmod tempor incididunt uted labore ete dolore magna minim veniamed, quised aliquad.</p>
    <div class="reviewer"><div class="avatar" role="img" aria-label="Reviewer portrait"></div><div><strong>Dana Holloway</strong><span class="stars">★★★★★</span></div></div>
    <span class="quote">“</span>
  </article>
</section>

<footer class="abs footer">
  <h4 style="left:64px">Our Cases</h4>
  <ul style="left:64px">
    <li>Clubs</li><li>Online Stores</li><li>Digital Products</li><li>Education</li><li>Coaching</li><li>Religious Organizations</li><li>Fitness</li>
  </ul>
  <h4 style="left:202px">Quick links</h4>
  <ul style="left:202px">
    <li>Home</li><li>About Us</li><li>Features</li><li>Testimonials</li><li>Contact Us</li>
  </ul>
  <h4 style="left:308px">Contact Us</h4>
  <div class="contact-row" style="top:75px"><span class="dot"><svg viewBox="0 0 10 10"><path d="M2 1l2 2-1 1.2c.6 1.3 1.5 2.2 2.8 2.8L7 6l2 2-1.3 1.3C4.5 9 1 5.5.7 2.3z" fill="#0aa3dd"/></svg></span><span style="padding-top:2px">+1 555 014 2290</span></div>
  <div class="contact-row" style="top:109px"><span class="dot"><svg viewBox="0 0 10 10"><rect x="1" y="2" width="8" height="6" fill="#0aa3dd"/><path d="M1 2l4 3 4-3" stroke="#fff" stroke-width=".8" fill="none"/></svg></span><span style="padding-top:2px">hello@tallowgatehubs.example</span></div>
  <div class="contact-row" style="top:137px"><span class="dot"><svg viewBox="0 0 10 10"><path d="M5 9.5S2 6 2 4a3 3 0 0 1 6 0c0 2-3 5.5-3 5.5z" fill="#0aa3dd"/><circle cx="5" cy="4" r="1" fill="#fff"/></svg></span><span>15000 .Lorem ipsum dolor<br>ameted adipiscinged elited</span></div>
  <h4 style="left:477px">Subscribe Newsletter</h4>
</footer>
<p class="abs newsletter-copy">Sign up today to get resources on how to attract and retain more customers!</p>
<div class="abs subscribe"><span><svg width="6" height="5" viewBox="0 0 6 5"><rect x=".3" y=".3" width="5.4" height="4.4" fill="none" stroke="#555" stroke-width=".5"/><path d="M.3.3 3 2.5 5.7.3" fill="none" stroke="#555" stroke-width=".5"/></svg>Email Address</span><b><svg width="10" height="10" viewBox="0 0 10 10"><path d="M9.5.5.5 4.5l3 1 1 3.5 1.8-2.4L9.5.5z" fill="#fff"/></svg></b></div>
<div class="abs social" style="left:477px" aria-label="Social link"></div>
<div class="abs social" style="left:500px" aria-label="Social link"></div>
<div class="abs social" style="left:522px" aria-label="Social link"></div>
<div class="abs social" style="left:544px" aria-label="Social link"></div>

<div class="abs copyright">©Copyrights 2022&nbsp; TallowGateHubs. All Rights Reserved.</div>
</body>
</html>
```